Unique Editable Recipe Cards

Create 10 unique editable recipe cards. Please look at Quonly and see what Editable Recipe cards are popular to get an idea of what Cards will sell. Search for "Editable Recipe Cards". The final images will need to be editable in Canva.

```html
<!DOCTYPE html>
<html lang="en">
<head>
<meta charset="utf-8">
<title>Sweet Apple Squares – Recipe Card</title>
<link rel="stylesheet" href="https://fonts.googleapis.com/css2?family=Noto+Serif:wght@400&family=Playfair+Display:ital@1&family=Mulish:wght@400&display=swap">
<style>
  :root {
    --paper: #fdf9f8;
    --ink: #141414;
    --ink-soft: #2a2a2a;
    --star-gold: #e8b923;
    --star-grey: #b9b9b9;
    --photo-light: #f4f1ee;
    --photo-mid: #ebe3db;
    --photo-warm: #dcc6ae;
    --rule: #1a1a1a;
  }
  * { box-sizing: border-box; margin: 0; padding: 0; }
  html, body { width: 851px; height: 1200px; overflow: hidden; }
  body { background: var(--paper); color: var(--ink); position: relative; font-family: "Mulish", sans-serif; }

  .recipe-title {
    position: absolute; left: 31px; top: 39px;
    font-family: "Noto Serif", serif; font-weight: 400; font-size: 45px; letter-spacing: 0.3px; white-space: nowrap;
  }
  .recipe-subtitle {
    position: absolute; left: 28px; top: 103px;
    font-family: "Playfair Display", serif; font-style: italic; font-size: 28px; white-space: nowrap;
  }
  .rating { position: absolute; left: 668px; top: 60px; display: flex; }
  .rating svg { width: 27px; height: 27px; }
  .star-on { fill: var(--star-gold); }
  .star-off { fill: var(--star-grey); }

  .hero-photo {
    position: absolute; left: 26px; top: 156px; width: 800px; height: 439px;
    background: linear-gradient(135deg, var(--photo-light) 0%, var(--photo-mid) 55%, var(--photo-warm) 100%);
  }

  .meta { position: absolute; top: 647px; left: 58px; display: flex; align-items: center; font-size: 14.5px; color: var(--ink-soft); }
  .meta-item { display: flex; align-items: center; }
  .meta-item svg { margin-right: 10px; }
  .meta-item + .meta-item { margin-left: 24px; }

  .column-rule { position: absolute; left: 323px; top: 645px; width: 2px; height: 488px; background: var(--rule); }

  .section-heading { font-family: "Noto Serif", serif; font-weight: 400; text-transform: uppercase; letter-spacing: 0.3px; }

  .ingredients { position: absolute; left: 49px; top: 711px; }
  .ingredients .section-heading { font-size: 25px; margin-bottom: 16px; }
  .ingredient-list { list-style: none; font-size: 18.5px; line-height: 32.6px; }

  .notes { position: absolute; left: 44px; top: 1038px; width: 238px; }
  .notes .section-heading { font-size: 21px; margin-bottom: 9px; }
  .notes p { font-size: 15.5px; line-height: 25px; }

  .directions { position: absolute; left: 370px; top: 652px; width: 450px; }
  .directions .section-heading { font-size: 25px; margin-bottom: 22px; }
  .direction-steps { list-style: none; counter-reset: step; font-size: 18.5px; line-height: 29.5px; }
  .direction-steps li { counter-increment: step; position: relative; padding-left: 18px; }
  .direction-steps li::before { content: counter(step) "."; position: absolute; left: 0; }
</style>
</head>
<body>
  <h1 class="recipe-title">Sweet Apple Squares</h1>
  <p class="recipe-subtitle">With cinnamon and thyme</p>

  <div class="rating" aria-label="Rated 4 out of 5">
    <svg viewBox="0 0 24 24"><path class="star-on" d="M12 2l2.9 6.9 7.1.6-5.4 4.7 1.7 7.3L12 17.7 5.7 21.5l1.7-7.3L2 9.5l7.1-.6z"/></svg>
    <svg viewBox="0 0 24 24"><path class="star-on" d="M12 2l2.9 6.9 7.1.6-5.4 4.7 1.7 7.3L12 17.7 5.7 21.5l1.7-7.3L2 9.5l7.1-.6z"/></svg>
    <svg viewBox="0 0 24 24"><path class="star-on" d="M12 2l2.9 6.9 7.1.6-5.4 4.7 1.7 7.3L12 17.7 5.7 21.5l1.7-7.3L2 9.5l7.1-.6z"/></svg>
    <svg viewBox="0 0 24 24"><path class="star-on" d="M12 2l2.9 6.9 7.1.6-5.4 4.7 1.7 7.3L12 17.7 5.7 21.5l1.7-7.3L2 9.5l7.1-.6z"/></svg>
    <svg viewBox="0 0 24 24"><path class="star-off" d="M12 2l2.9 6.9 7.1.6-5.4 4.7 1.7 7.3L12 17.7 5.7 21.5l1.7-7.3L2 9.5l7.1-.6z"/></svg>
  </div>

  <div class="hero-photo" role="img" aria-label="Overhead photo of apple squares topped with sliced apples on white plates with forks, on a marble table"></div>

  <div class="meta">
    <div class="meta-item">
      <svg width="16" height="30" viewBox="0 0 16 30" fill="none" stroke="#333" stroke-width="1.4">
        <path d="M1 1v8a2.5 2.5 0 0 0 5 0V1M3.5 1v28"/>
        <path d="M14 1c-3 1-4 5-4 10h4v18h-2V11"/>
      </svg>
      <span>2 servings</span>
    </div>
    <div class="meta-item">
      <svg width="24" height="24" viewBox="0 0 24 24" fill="none" stroke="#333" stroke-width="1.8">
        <circle cx="12" cy="12" r="10.5"/><path d="M12 6v6l4 3"/>
      </svg>
      <span>15 minutes</span>
    </div>
  </div>

  <div class="column-rule"></div>

  <section class="ingredients">
    <h2 class="section-heading">Ingredients</h2>
    <ul class="ingredient-list">
      <li>100 ml milk</li>
      <li>50 g butter</li>
      <li>3 eggs</li>
      <li>1 tbs cocoa</li>
      <li>2 tsp baking soda</li>
      <li>a pinch of salt</li>
      <li>3 eggs</li>
    </ul>
  </section>

  <section class="notes">
    <h2 class="section-heading">Notes</h2>
    <p>Nunc nulla velit, feugiat vitae ex quis, lobortis porta leo. Donec dictum lectus.</p>
  </section>

  <section class="directions">
    <h2 class="section-heading">Directions</h2>
    <ol class="direction-steps">
      <li>Nunc nulla velit, feugiat vitae ex quis, lobortis porta leo.</li>
      <li>Donec dictum lectus in ex accumsan sodales. Pellentesque habitant morbi tristique.</li>
      <li>Nunc nulla velit, feugiat vitae ex quis, lobortis porta leo. Donec dictum lectus in ex. lentesque habitant morbi tristique. Nunc nulla velit, feugiat vitae ex quis, lobortis porta leo. Donec dictum lectus in ex.</li>
      <li>Habitant morbi tristique.Nunc nulla velit, feugiat vitae ex quis, lobortis porta leo. Donec dictum lectu,</li>
      <li>Donec dictum lectus in ex accumsan sodales. Pellentesque habitant morbi tristique.</li>
    </ol>
  </section>
</body>
</html>
```